Successful Software Co Launching A Super FUN Mobile & Web Application - ROCKSTAR Designer Needed

Our App is called "Sparkle Pennant"It is an employee "gamification" app designed to make working at your job fun...Employees complete simple tasks throughout the work day and are rewarded with points they can redeem for different gifts and benefits...We an AMAZING User Interface designed for both the mobile app and website app. We are looking for a clean, modern and simple design... This app is designed to make employees more engaged at work while having fun doing the things they already do each day...They can then redeem their points for rewards. It needs to be easy to understand and simple in its design...Example: A local carpet cleaning business uses our app.Their employees show up to work on time - They get 50 pointsThey clean out their work vehicle - They get 100 pointsThey up-sell an additional cleaning job - The get 250 pointsEtc...The app will also have fun icons and graphics that appear on the screen when an employee accomplishes a task.The app will play fun music sounds when they accomplish tasks too.
Updates

Need extra days to review

Target Market(s)

Small business owners

Logo Text

Sparkle Pennant

Font styles to use
Sans Serif

Colors

Designer to choose colors to be used in the design.

Requirements
Must have
• Simple elegant design
Nice to have
• I'd like to see examples of fun "icons" that could pop up on the screen after an employee completes a "task" and earns points... Something fun to pop up on the screen... (like a happy face, a thumbs up, fun text bubbles... "Way To Go!" etc... or any other fun ideas)

```html
<!DOCTYPE html>
<html lang="en">
<head>
<meta charset="utf-8">
<title>Sparkle Pennant – Rewards</title>
<link rel="stylesheet" href="https://fonts.googleapis.com/css2?family=Montserrat:wght@700&family=Mulish:wght@400;500;600&display=swap">
<style>
  :root {
    --sky: #3cb0f8;
    --mid: #3a78c8;
    --night: #35306e;
    --white: #ffffff;
    --ink: #2a2a35;
    --muted: #c4c8cf;
    --accent: #1fb6e4;
    --track: #3aaef5;
  }
  * { margin: 0; padding: 0; box-sizing: border-box; }
  html, body { width: 675px; height: 1200px; overflow: hidden; }
  body {
    position: relative;
    font-family: "Mulish", sans-serif;
    color: var(--white);
    background: linear-gradient(180deg, var(--sky) 0%, var(--mid) 50%, var(--night) 100%);
  }
  .status-bar {
    position: absolute; top: 0; left: 0; width: 675px; height: 36px;
    display: flex; align-items: center; justify-content: space-between;
    padding: 0 18px; font-size: 20px; font-weight: 500;
  }
  .status-left, .status-right { display: flex; align-items: center; gap: 8px; }
  .app-title {
    position: absolute; top: 80px; width: 100%; text-align: center;
    font-family: "Montserrat", sans-serif; font-weight: 700; font-size: 29px; letter-spacing: .3px;
  }
  .reward-search {
    position: absolute; left: 27px; top: 160px; width: 621px; height: 71px;
    background: var(--white); border-radius: 6px;
    display: flex; align-items: center; justify-content: space-between; padding: 0 24px 0 27px;
    font-size: 15.5px; color: var(--ink);
  }
  .reward-search .hint { color: var(--muted); }
  .goal-label {
    position: absolute; top: 260px; width: 100%; text-align: center; font-size: 22px;
  }
  .goal-track {
    position: absolute; left: 87px; top: 322px; width: 502px; height: 22px;
    background: var(--white); border-radius: 11px; overflow: hidden;
  }
  .goal-fill {
    width: 207px; height: 100%; background: var(--track);
    border: 2px solid var(--white); border-radius: 11px 0 0 11px;
  }
  .goal-thumb { position: absolute; left: 273px; top: 311px; }
  .goal-ticks { position: absolute; left: 108px; top: 361px; }
  .points-total {
    position: absolute; top: 400px; width: 100%; text-align: center; font-size: 21px;
  }
  .history-button {
    position: absolute; left: 235px; top: 461px; width: 205px; height: 58px;
    border: 2px solid var(--white); border-radius: 8px;
    display: flex; align-items: center; justify-content: center;
    font-size: 15.5px; font-weight: 600; letter-spacing: .2px;
  }
  .task-card {
    position: absolute; left: 28px; width: 620px; height: 107px;
    background: var(--white); border-radius: 6px; color: var(--ink);
    display: flex; align-items: center; justify-content: space-between;
    padding: 0 28px 0 26px; font-size: 16.5px;
  }
  .task-points {
    width: 132px; height: 54px; border: 2px solid var(--accent); border-radius: 7px;
    color: var(--accent); font-size: 15.5px; font-weight: 500;
    display: flex; align-items: center; justify-content: center;
  }
  .action-button {
    position: absolute; top: 1089px; width: 207px; height: 59px;
    background: var(--accent); border-radius: 6px;
    display: flex; align-items: center; justify-content: center;
    font-size: 15.5px; font-weight: 600; letter-spacing: -.2px;
  }
</style>
</head>
<body>
  <div class="status-bar">
    <div class="status-left">
      <svg width="56" height="12" viewBox="0 0 56 12" aria-hidden="true">
        <circle cx="6" cy="6" r="5" fill="#fff"/><circle cx="17" cy="6" r="5" fill="#fff"/>
        <circle cx="28" cy="6" r="5" fill="#fff"/><circle cx="39" cy="6" r="5" fill="#fff"/>
        <circle cx="50" cy="6" r="4.3" fill="none" stroke="#fff" stroke-width="1.2"/>
      </svg>
      <span>Carrier</span>
      <svg width="20" height="15" viewBox="0 0 20 15" aria-hidden="true">
        <path d="M10 14 L6.5 10.2 A5 5 0 0 1 13.5 10.2 Z" fill="#fff"/>
        <path d="M3.8 7.6 A9 9 0 0 1 16.2 7.6" stroke="#fff" stroke-width="2.2" fill="none"/>
        <path d="M1 4.6 A13 13 0 0 1 19 4.6" stroke="#fff" stroke-width="2.2" fill="none"/>
      </svg>
    </div>
    <div class="status-right">
      <svg width="18" height="18" viewBox="0 0 18 18" aria-hidden="true">
        <circle cx="9" cy="9" r="7.5" fill="none" stroke="#fff" stroke-width="1.6"/>
        <rect x="6" y="8" width="6" height="5" fill="#fff"/>
        <path d="M7 8 V6.5 A2 2 0 0 1 11 6.5 V8" fill="none" stroke="#fff" stroke-width="1.3"/>
      </svg>
      <span>100%</span>
      <svg width="40" height="18" viewBox="0 0 40 18" aria-hidden="true">
        <rect x="1" y="1" width="34" height="16" rx="3" fill="none" stroke="#fff" stroke-width="1.5"/>
        <rect x="3.5" y="3.5" width="29" height="11" rx="1.5" fill="#fff"/>
        <rect x="36.5" y="6" width="2.5" height="6" rx="1" fill="#fff"/>
      </svg>
    </div>
  </div>

  <h1 class="app-title">WELCOME TO SPARKLE PENNANT, NORA</h1>

  <div class="reward-search">
    <p>Your are only 75 Points Away <span class="hint">From Your Next Reward</span></p>
    <svg width="36" height="36" viewBox="0 0 36 36" aria-label="Search" role="img">
      <circle cx="14.5" cy="14.5" r="10.5" fill="none" stroke="#1fb6e4" stroke-width="4.5"/>
      <line x1="22.5" y1="22.5" x2="32" y2="32" stroke="#1fb6e4" stroke-width="5.5" stroke-linecap="round"/>
    </svg>
  </div>

  <p class="goal-label">Montily Goal : 3,000 Point</p>
  <div class="goal-track"><div class="goal-fill"></div></div>
  <svg class="goal-thumb" width="42" height="46" viewBox="0 0 42 46" aria-hidden="true">
    <path d="M21 44 L5 30 A19 19 0 1 1 37 30 Z" fill="#fff" stroke="#c9ced6" stroke-width="1.2"/>
  </svg>
  <svg class="goal-ticks" width="460" height="13" viewBox="0 0 460 13" aria-hidden="true">
    <g stroke="#fff" stroke-width="2">
      <line x1="1" y1="0" x2="1" y2="13"/><line x1="46.7" y1="0" x2="46.7" y2="13"/>
      <line x1="92.4" y1="0" x2="92.4" y2="13"/><line x1="138.1" y1="0" x2="138.1" y2="13"/>
      <line x1="183.8" y1="0" x2="183.8" y2="13"/><line x1="229.5" y1="0" x2="229.5" y2="13"/>
      <line x1="275.2" y1="0" x2="275.2" y2="13"/><line x1="320.9" y1="0" x2="320.9" y2="13"/>
      <line x1="366.6" y1="0" x2="366.6" y2="13"/><line x1="412.3" y1="0" x2="412.3" y2="13"/>
      <line x1="458" y1="0" x2="458" y2="13"/>
    </g>
  </svg>
  <p class="points-total">Your currently have 2.250 Points</p>

  <div class="history-button">REWARD HISTORY</div>

  <div class="task-card" style="top:562px"><p>Show up on time every day for month</p><div class="task-points">100 POINTS</div></div>
  <div class="task-card" style="top:689px"><p>Up-Sell Over $250 in Services</p><div class="task-points">250 POINTS</div></div>
  <div class="task-card" style="top:818px"><p>Pass your vehicle inspection report each week</p><div class="task-points">50 POINTS</div></div>
  <div class="task-card" style="top:946px"><p>Daily paperwork&nbsp; turned in complate on time</p><div class="task-points">150 POINTS</div></div>

  <div class="action-button" style="left:27px">CONTACT EMPLOYER</div>
  <div class="action-button" style="left:441px">REQUEST TIME OFF</div>
</body>
</html>
```